Real Estate Marketing Postcards need a fresh look, Front & Back

I have a current postcard design (attached) that lacks design quality and too much use of color. I do like the basic color scheme, but I'm open to anything that cleans up the look and incorporates space for the existing text. I'm not opposed to a design with a white background, more white space. The design should be full bleed according to the attached specs. I would like this to be sent over in an Adobe format, something like InDesign.

The company logo will remain the same colors and appearance. The headshot will likely be updated in the coming weeks.

I am attaching a sample of a recent card plus a template from the printer showing the back of the card and location of the address and postage section that must remain blank. I am also including the logo and another logo designed for use with a white (or non blue) background.

(feel free to swap in stock photos of whatever house you want, but the front of the card should incorporate at least one photo of a house.)

Target Market(s)

Home owners.

Industry/Entity Type

Real Estate

Font styles to use
Sans Serif

Colors

Designer to choose colors to be used in the design.

Requirements
Must have
• Company logo, the headshot, the contact info on the back, a photo or photos of a house along with the text "Just Sold" or "Sold" featured on the front of the card.

```html
<!DOCTYPE html>
<html lang="en">
<head>
<meta charset="utf-8">
<title>Oakridge Realtor Postcard — Front &amp; Back</title>
<link href="https://fonts.googleapis.com/css2?family=Montserrat:wght@600;700&family=Open+Sans:wght@400;600;700&display=swap" rel="stylesheet">
<style>
  :root {
    --lime: #a3c232;
    --navy: #1b3f6b;
    --ink: #1e1e1e;
    --sky-blue: #8ec9ee;
    --paper: #ffffff;
    --panel-grey: #ebebeb;
    --stage: #e9e7e4;
  }
  * { margin: 0; padding: 0; box-sizing: border-box; }
  html, body { width: 1200px; height: 510px; overflow: hidden; }
  body {
    background: var(--stage);
    position: relative;
    font-family: "Open Sans", Arial, sans-serif;
  }
  .postcard {
    position: absolute;
    top: 88px;
    width: 478px;
    height: 336px;
    background: var(--paper);
    overflow: hidden;
  }
  .postcard--front { left: 118px; }
  .postcard--back { left: 616px; }

  /* Front */
  .house-photo {
    position: absolute; inset: 0;
    background: linear-gradient(180deg,
      #8f8eb6 0%, #a9a2c0 22%, #7c8191 40%, #5d6472 58%,
      #7d838c 70%, #b9bcc2 82%, #d9dbdf 100%);
  }
  .front-overlay { position: absolute; inset: 0; }
  .front-headline {
    position: absolute;
    right: 24px;
    bottom: 18px;
    text-align: right;
  }
  .front-headline__sold {
    font-family: "Montserrat", Arial, sans-serif;
    font-weight: 700;
    font-size: 33px;
    line-height: 1;
    color: var(--lime);
    letter-spacing: -0.5px;
  }
  .front-headline__title {
    font-family: "Montserrat", Arial, sans-serif;
    font-weight: 700;
    font-size: 23px;
    line-height: 1.15;
    color: var(--navy);
    letter-spacing: 1.5px;
    margin-top: 4px;
  }
  .front-headline__tagline {
    font-size: 14px;
    color: var(--ink);
    margin-top: 3px;
  }

  /* Back */
  .back-heading {
    position: absolute;
    top: 30px; left: 0; right: 0;
    text-align: center;
    font-family: "Montserrat", Arial, sans-serif;
    font-weight: 600;
    font-size: 35px;
    letter-spacing: 5px;
    color: var(--lime);
  }
  .back-pitch {
    position: absolute;
    top: 88px; left: 0; right: 0;
    text-align: center;
    font-size: 10.5px;
    font-weight: 600;
    line-height: 1.4;
    letter-spacing: 1px;
    color: var(--ink);
  }
  .headshot-frame {
    position: absolute;
    left: 21px; top: 142px;
    width: 95px; height: 96px;
    border: 3px solid var(--navy);
    background: var(--paper);
    padding: 6px;
  }
  .headshot {
    width: 100%; height: 100%;
    background: linear-gradient(180deg, #9a9aa0, #c4c2c2);
  }
  .brand-name {
    position: absolute;
    left: 150px; top: 176px;
    display: flex; align-items: center; gap: 8px;
    font-weight: 700;
    font-size: 22px;
    color: var(--navy);
  }
  .brand-name__mark {
    width: 14px; height: 14px;
    background: var(--sky-blue);
  }
  .agent-contact {
    position: absolute;
    left: 334px; top: 153px;
    font-size: 9px;
    font-weight: 600;
    line-height: 11.3px;
    letter-spacing: 0.5px;
    color: var(--ink);
    list-style: none;
  }
  .agent-divider {
    position: absolute;
    left: 116px; top: 235px;
    width: 342px; height: 2px;
    background: var(--navy);
  }
  .mailing-area {
    position: absolute;
    left: 0; right: 0; bottom: 0;
    height: 88px;
    background: linear-gradient(180deg, var(--panel-grey), #f6f6f6);
  }
</style>
</head>
<body>
  <section class="postcard postcard--front">
    <div class="house-photo" role="img" aria-label="Photo of a two-storey grey house with lit windows and a double garage at dusk"></div>
    <svg class="front-overlay" viewBox="0 0 478 336" width="478" height="336" aria-hidden="true">
      <polygon points="0,210 478,250 478,336 0,336" fill="#ffffff" fill-opacity="0.45"/>
      <polygon points="0,262 478,228 478,336 0,336" fill="#ffffff" fill-opacity="0.35"/>
    </svg>
    <div class="front-headline">
      <div class="front-headline__sold">JUST SOLD!</div>
      <div class="front-headline__title">THE OAKRIDGE REALTOR</div>
      <div class="front-headline__tagline">You Know It Won't Last Long!</div>
    </div>
  </section>

  <section class="postcard postcard--back">
    <h2 class="back-heading">SELLING?</h2>
    <p class="back-pitch">There is no other agent who knows the Oakridge market better.<br>Contact me today to get your home SOLD.</p>
    <div class="headshot-frame">
      <div class="headshot" role="img" aria-label="Agent headshot"></div>
    </div>
    <div class="brand-name"><span class="brand-name__mark"></span>Willow Bend</div>
    <ul class="agent-contact">
      <li>Marco Delvecchio</li>
      <li>“The Oakridge Realtor</li>
      <li>Willow Bend Real Estate</li>
      <li>(301) 555-0142 Office</li>
      <li>(301) 555-0187 Cell</li>
      <li>www.oakridgekeyhomes.com</li>
    </ul>
    <div class="agent-divider"></div>
    <div class="mailing-area"></div>
  </section>
</body>
</html>
```